Business Card Design Project

Industry/Entity Type

Business

Contact Information for Business Card

The Harlow Vale Gospel Choir
Dean Marsell, Minister of Music

The Coastal Wesleyan Church of Bramford Hill
Founded 1792

Twitter @thehvgc
Instagram harlowvalegc
Facebook facebook.com/hvgc408
Website: harlowvalegc-example.org
For Bookings: (555) 204-HVGC
4287 Bramwell Street, Philadelphia, PA 19874

Back of the Card
Music and Cd's Recordings Available On
Choirs Website and Also
Tunevox, Orbala Sound, Disc Sprout (the music online logo)

```html
<!DOCTYPE html>
<html lang="en">
<head>
<meta charset="utf-8">
<title>The Harlow Vale Gospel Choir — Card Back</title>
<link rel="stylesheet" href="https://fonts.googleapis.com/css2?family=Roboto:wght@700&display=swap">
<style>
  :root {
    --card-black: #070809;
    --edge-red: #e0264a;
    --type-white: #ffffff;
    --sprout-lime: #c5d32f;
  }
  html, body {
    margin: 0;
    padding: 0;
    width: 1200px;
    height: 719px;
    overflow: hidden;
    background: var(--card-black);
  }
  .card-back {
    position: relative;
    box-sizing: border-box;
    width: 1200px;
    height: 719px;
    background: var(--card-black);
    border: 1px solid var(--edge-red);
  }
  .availability {
    position: absolute;
    left: 112px;
    top: 259px;
    margin: 0;
    font-family: "Roboto", "Helvetica Neue", Arial, sans-serif;
    font-weight: 700;
    font-size: 36px;
    line-height: 45px;
    letter-spacing: 0.09em;
    text-transform: uppercase;
    color: var(--type-white);
  }
  .availability__line {
    display: block;
    white-space: nowrap;
  }
  .availability__store {
    color: var(--sprout-lime);
    text-transform: none;
    letter-spacing: 0.02em;
    margin-left: 6px;
  }
</style>
</head>
<body>
  <main class="card-back">
    <p class="availability">
      <span class="availability__line">Music and CD Recordings</span>
      <span class="availability__line">Available on Choir Website,</span>
      <span class="availability__line">Tunevox, Orbala Sound,</span>
      <span class="availability__line">&amp; <span class="availability__store">Disc Sprout</span></span>
    </p>
  </main>
</body>
</html>
```